Quorvia medical teaching of the future

responsive website, onepager, for medical technology company. It has to look clean and high tech.

Look & feel
• Responsive
• Clean
• Combination icons + foto's
• Integration of a YouTube video

Landingpage items

• Header: picture + 'a video-based teaching platform for surgical procedures'
• About Deferred live medical teaching: Short description
• Features
o Video
o Teaching platform

• Benefits:
o More effective learning
o Faster sharing of knowledge & tecniques
o More cost effective

• References

• Products:
o Live (+link to more info)
o bTamo (+ link to more info)
o bTamo local (+link to more info)
o bTamo cloud (+ link to more info)

• Solutions:
o For medical device companies (+link to more info)
o Doctor and surgeons (+link to more info)
o Medical conferences (+link to more info)

Target Market(s)

medical device companies
surgeons and doctors
conference organisers

Industry/Entity Type

It Company

Number of Pages Required

1 page

Requirements
Must have
• Landingpage items
• • Header: picture + 'a video-based teaching platform for surgical procedures'
• • About Deferred live medical teaching: Short description
• • Features
• o Video
• o Teaching platform
• • Benefits:
• o More effective learning
• o Faster sharing of knowledge & tecniques
• o More cost effective
• • References
• • Products:
• o Live (+link to more info)
• o bTamo (+ link to more info)
• o bTamo local (+link to more info)
• o bTamo cloud (+ link to more info)
• • Solutions:
• o For medical device companies (+link to more info)
• o Doctor and surgeons (+link to more info)
• o Medical conferences (+link to more info)
Nice to have
• possibilty to show video

```html
<!DOCTYPE html>
<html lang="en">
<head>
<meta charset="utf-8">
<title>Quorvia – medical teaching of the future</title>
<link href="https://fonts.googleapis.com/css2?family=Open+Sans:wght@400;600&family=Roboto:wght@400;500&display=swap" rel="stylesheet">
<style>
:root{
  --teal:#339b93;
  --teal-dark:#267a74;
  --teal-deep:#1f5a56;
  --red:#e0002a;
  --red-dark:#b7102c;
  --grey:#aaa6a6;
  --grey-dark:#7e7b7b;
  --ink:#1d1d1d;
  --white:#ffffff;
  --light:#efeeee;
  --footer:#0d3b3a;
}
*{margin:0;padding:0;box-sizing:border-box}
html,body{width:1200px;height:1200px;overflow:hidden;background:var(--white)}
body{position:relative;font-family:"Open Sans",sans-serif;color:var(--ink)}
.abs{position:absolute}
h2,h3,.brand,.nav a{font-family:"Roboto",sans-serif;font-weight:400}

/* header */
.site-header{left:0;top:0;width:1200px;height:85px}
.brand{left:133px;top:22px;display:flex;align-items:center;gap:10px;font-size:34px;color:var(--teal)}
.brand-dot{width:38px;height:38px;border-radius:50%;background:var(--teal)}
.nav{left:490px;top:24px;display:flex;align-items:center;height:46px}
.nav a{font-size:13.6px;color:var(--red);text-decoration:none;margin-right:33px}
.nav a.active{background:var(--teal);color:var(--white);padding:0 16px;height:46px;line-height:46px;border-radius:3px;margin-right:18px}

/* hero */
.hero{left:0;top:85px;width:1200px;height:285px;background:linear-gradient(120deg,#4f6a69,#8aa4a2 45%,#5f7977 70%,#9db1af)}
.hero-video{left:133px;top:45px;width:328px;height:214px;background:linear-gradient(160deg,#4c5b5c,#2f3e3f)}
.play{position:absolute;left:50%;top:50%;transform:translate(-50%,-50%)}
.hero-title{left:512px;top:100px;width:556px;height:48px;background:rgba(40,40,40,.72);color:var(--red);font-size:19px;text-align:center;line-height:48px;font-family:"Open Sans",sans-serif}
.hero-text{left:512px;top:166px;width:556px;height:90px;background:rgba(40,40,40,.72);color:var(--white);font-family:"Roboto",sans-serif;font-size:13.4px;line-height:22.4px;padding:12px 18px}

/* about & features */
.about-band{left:0;top:370px;width:1200px;height:211px;background:var(--grey)}
.about-shape{left:0;top:0}
.about{left:133px;top:12px;width:300px;color:var(--white)}
.about h2{font-size:20px;margin-top:70px;color:var(--ink)}
.rule{display:block;width:45px;height:2px;background:var(--teal);margin:9px 0 10px}
.about .rule{background:#cfe7e4}
.about p{font-size:12px;line-height:16px}
.about-icon{left:97px;top:-3px}
.features{left:534px;top:12px;width:540px}
.features h2{font-size:20px;color:var(--ink)}
.features .rule{margin-top:8px}
.features-video{left:0;top:42px;width:214px;height:134px;background:linear-gradient(160deg,#56605f,#2e3a3a)}
.feature-list{left:238px;top:44px;width:270px;list-style:none;color:var(--white);font-size:12px;line-height:16px}
.feature-list li{position:relative;padding-left:24px;margin-bottom:8px}
.feature-list svg{position:absolute;left:0;top:0}

/* benefits */
.benefits-title{left:0;top:585px;width:1200px;text-align:center;font-size:20px}
.benefits-rule{left:577px;top:615px;width:45px;height:2px;background:var(--teal)}
.benefits-intro{left:0;top:624px;width:1200px;text-align:center;font-family:"Roboto",sans-serif;font-size:11.6px;color:#333}
.card{width:296px;height:132px;top:654px;color:var(--white)}
.card.red{left:133px;background:var(--red)}
.card.teal{left:453px;background:var(--teal)}
.card.grey{left:773px;background:var(--grey)}
.card-icon{position:absolute;left:14px;top:8px;width:84px;height:84px;border-radius:50%}
.red .card-icon{background:var(--red-dark)}
.teal .card-icon{background:var(--teal-dark)}
.grey .card-icon{background:var(--grey-dark)}
.card-icon svg{position:absolute;left:50%;top:50%;transform:translate(-50%,-50%)}
.card-body{position:absolute;left:109px;top:7px;width:180px}
.card h3{font-size:16px;line-height:16.5px;color:var(--ink)}
.card .rule{background:var(--ink);margin:5px 0 6px}
.card p{font-size:12px;line-height:16px}
.ribbon{top:790px}

/* products */
.products{left:0;top:826px;width:1200px;height:169px;background:linear-gradient(100deg,#2b5d5a,#3d706c 40%,#2c5a57 70%,#3b6b67)}
.products h2{position:absolute;left:0;top:4px;width:1200px;text-align:center;color:var(--white);font-size:20px}
.products .section-rule{position:absolute;left:577px;top:35px;width:45px;height:2px;background:var(--teal)}
.product{top:51px;width:215px;height:110px;background:rgba(120,140,140,.45)}
.product-photo{position:absolute;left:7px;top:9px;width:94px;height:94px;border-radius:50%;border:3px solid var(--teal)}
.product-name{position:absolute;left:110px;top:27px;width:100px;text-align:center;color:var(--white);font-family:"Roboto",sans-serif;font-size:14.4px}
.product-name.small{font-size:12.4px}
.btn{display:block;background:var(--teal);color:var(--white);font-family:"Roboto",sans-serif;font-size:13.4px;text-align:center;text-decoration:none;width:95px;height:37px;line-height:37px;border-radius:2px}
.product .btn{position:absolute;left:112px;top:65px}

/* solutions */
.solutions{left:0;top:995px;width:1200px;height:183px;background:var(--light)}
.solutions h2{position:absolute;left:0;top:3px;width:1200px;text-align:center;font-size:20px}
.solutions .section-rule{position:absolute;left:577px;top:35px;width:45px;height:2px;background:var(--teal)}
.solution{top:44px;width:295px}
.solution-photo{position:relative;height:87px}
.solution-caption{position:absolute;left:0;bottom:0;width:100%;height:22px;background:rgba(30,40,40,.55);color:var(--white);font-size:14px;line-height:22px;padding-left:6px}
.solution .btn{margin:8px auto 0}

.site-footer{left:0;top:1178px;width:1200px;height:22px;background:var(--footer);color:var(--white);font-size:9.6px;text-align:center;line-height:22px}
</style>
</head>
<body>

<header class="site-header abs">
  <div class="brand abs"><span class="brand-dot"></span>Quorvia</div>
  <nav class="nav abs">
    <a class="active" href="#">Home</a>
    <a href="#">About Us</a>
    <a href="#">Features</a>
    <a href="#">Benifits</a>
    <a href="#">Products</a>
    <a href="#">Solutions</a>
    <a href="#">Contact</a>
  </nav>
</header>

<section class="hero abs" role="img" aria-label="Surgeons in an operating room with monitors">
  <div class="hero-video abs" role="img" aria-label="Video still of a surgical team in theatre">
    <svg class="play" width="22" height="24" viewBox="0 0 22 24"><path d="M0 0L22 12L0 24Z" fill="#fff"/></svg>
  </div>
  <div class="hero-title abs">Quorvia changes the way medical procedures are taught.</div>
  <div class="hero-text abs">Quorvia is building a video based cloud teaching platform for all kinds of medical procedures using synchronized high resolution 360° and wide angle videos in a virtual reality environment.</div>
</section>

<section class="about-band abs">
  <svg class="about-shape abs" width="503" height="211"><path d="M0 0H503L446 211H0Z" fill="var(--teal)"/></svg>
  <div class="about abs">
    <svg class="about-icon abs" width="54" height="54" viewBox="0 0 54 54" fill="none" stroke="#fff" stroke-width="3">
      <rect x="20" y="6" width="30" height="44" rx="2"/>
      <rect x="29" y="2" width="12" height="7" fill="#fff"/>
      <path d="M30 20H44M30 28H44M30 36H44M30 44H44"/>
      <path d="M4 14L18 9L32 14V27C32 37 25 43 18 46C11 43 4 37 4 27Z" fill="#fff" stroke="var(--teal)"/>
      <path d="M18 20V36M10 28H26" stroke="var(--teal)" stroke-width="5"/>
    </svg>
    <h2>Deferred live medical teaching</h2>
    <span class="rule"></span>
    <p>Healthcare companies contract top surgeons to do teaching sessions with their appliances/equipment. In the case of peer-to-peer medical teachings, medical device companies fly in surgeons from all over the world to attend live surgeries.</p>
  </div>
  <div class="features abs">
    <h2>Teaching Platform for medical procedures</h2>
    <span class="rule"></span>
    <div class="features-video abs" role="img" aria-label="Video still of a surgical procedure being filmed">
      <svg class="play" width="22" height="24" viewBox="0 0 22 24"><path d="M0 0L22 12L0 24Z" fill="#fff"/></svg>
    </div>
    <ul class="feature-list abs">
      <li><svg width="16" height="16" viewBox="0 0 16 16" fill="none" stroke="#555" stroke-width="1.5"><path d="M8 1L14 3V8C14 11.5 11 14 8 15C5 14 2 11.5 2 8V3Z"/><path d="M5 8L7 10L11 6"/></svg>Immersive cloud based teaching platform</li>
      <li><svg width="16" height="16" viewBox="0 0 16 16" fill="none" stroke="#555" stroke-width="1.5"><path d="M8 1L14 3V8C14 11.5 11 14 8 15C5 14 2 11.5 2 8V3Z"/><path d="M5 8L7 10L11 6"/></svg>Based on high resolution wide-angle 360° video capturing of surgical procedures</li>
      <li><svg width="16" height="16" viewBox="0 0 16 16" fill="none" stroke="#555" stroke-width="1.5"><path d="M8 1L14 3V8C14 11.5 11 14 8 15C5 14 2 11.5 2 8V3Z"/><path d="M5 8L7 10L11 6"/></svg>Multiple synchronized cameras</li>
      <li><svg width="16" height="16" viewBox="0 0 16 16" fill="none" stroke="#555" stroke-width="1.5"><path d="M8 1L14 3V8C14 11.5 11 14 8 15C5 14 2 11.5 2 8V3Z"/><path d="M5 8L7 10L11 6"/></svg>A single person performs capturing with no need to access the OR</li>
    </ul>
  </div>
</section>

<h2 class="benefits-title abs">Benefits</h2>
<span class="benefits-rule abs"></span>
<p class="benefits-intro abs">Medical and surgical knowledge can be shared in a faster, easier and more cost-effective way than current solutions like movies and pre-edited video.</p>

<article class="card red abs">
  <div class="card-icon"><svg width="48" height="46" viewBox="0 0 48 46"><rect x="0" y="0" width="48" height="38" fill="#fff"/><path d="M0 40H48M0 44H48" stroke="#fff" stroke-width="2"/><path d="M24 6V32M16 10H32" stroke="var(--red)" stroke-width="3"/><path d="M18 16C30 18 18 24 30 26" stroke="var(--red)" stroke-width="2" fill="none"/></svg></div>
  <div class="card-body">
    <h3>More effective learning</h3><span class="rule"></span>
    <p>Easier learning due to advanced video-based interactivity and state of the art medical illustrations clarifying each step of the procedure</p>
  </div>
</article>
<article class="card teal abs">
  <div class="card-icon"><svg width="58" height="58" viewBox="0 0 58 58" fill="none" stroke="#fff" stroke-width="4"><ellipse cx="29" cy="29" rx="26" ry="10"/><ellipse cx="29" cy="29" rx="26" ry="10" transform="rotate(60 29 29)"/><ellipse cx="29" cy="29" rx="26" ry="10" transform="rotate(120 29 29)"/></svg></div>
  <div class="card-body">
    <h3>Faster sharing of knowledge &amp; tecniques</h3><span class="rule"></span>
    <p>Faster sharing of knowledge and new techniques to surgeons worldwide due to the cloud-based teaching platform</p>
  </div>
</article>
<article class="card grey abs">
  <div class="card-icon"><svg width="34" height="66" viewBox="0 0 34 66"><text x="17" y="50" text-anchor="middle" font-family="Roboto,sans-serif" font-size="58" font-weight="500" fill="#fff">$</text><path d="M10 54L17 64L24 54Z" fill="#fff"/></svg></div>
  <div class="card-body">
    <h3>More cost effective</h3><span class="rule"></span>
    <p>More cost-effective compared to traditional teaching methods</p>
  </div>
</article>
<svg class="ribbon abs" style="left:133px" width="296" height="27"><path d="M0 0H296V27L150 12L0 27Z" fill="var(--red-dark)"/><path d="M0 0H296L150 12L0 27Z" fill="var(--red)" opacity=".6"/></svg>
<svg class="ribbon abs" style="left:453px" width="296" height="27"><path d="M0 0H296V27L150 12L0 27Z" fill="var(--teal-dark)"/><path d="M0 0H296L150 12L0 27Z" fill="var(--teal)" opacity=".6"/></svg>
<svg class="ribbon abs" style="left:773px" width="296" height="27"><path d="M0 0H296V27L150 12L0 27Z" fill="#c9c7c7"/><path d="M0 0H296L150 12L0 27Z" fill="var(--grey-dark)" opacity=".9"/></svg>

<section class="products abs" role="img" aria-label="Dimmed operating room photo background">
  <h2>Products</h2><span class="section-rule"></span>
  <div class="product abs" style="left:134px"><div class="product-photo" role="img" aria-label="Capture equipment case" style="background:linear-gradient(140deg,#d7dada,#5c6466)"></div><span class="product-name small">Live</span><a class="btn" href="#">More Info</a></div>
  <div class="product abs" style="left:374px"><div class="product-photo" role="img" aria-label="Surgeons operating" style="background:linear-gradient(140deg,#8aa9b0,#3d5a62)"></div><span class="product-name">bTamo</span><a class="btn" href="#">More Info</a></div>
  <div class="product abs" style="left:614px"><div class="product-photo" role="img" aria-label="Surgeon beside equipment tower" style="background:linear-gradient(140deg,#bcc6cc,#4e6a86)"></div><span class="product-name">bTamo Local</span><a class="btn" href="#">More Info</a></div>
  <div class="product abs" style="left:854px"><div class="product-photo" role="img" aria-label="Surgeon with head camera" style="background:linear-gradient(140deg,#a7b9b6,#4e7570)"></div><span class="product-name">bTamo Cloud</span><a class="btn" href="#">More Info</a></div>
</section>

<section class="solutions abs">
  <h2>Solutions</h2><span class="section-rule"></span>
  <div class="solution abs" style="left:133px"><div class="solution-photo" role="img" aria-label="Surgical team with colourful monitor screens" style="background:linear-gradient(100deg,#7a6c68,#5b5fa0 45%,#3f6ea8)"><span class="solution-caption">For Medical Device Companies</span></div><a class="btn" href="#">More Info</a></div>
  <div class="solution abs" style="left:453px"><div class="solution-photo" role="img" aria-label="Surgeons watching an endoscopy monitor" style="background:linear-gradient(100deg,#7fa9a4,#a54a9a 45%,#6fb0b3 70%,#3e5a66)"><span class="solution-caption">Doctor and Surgeons</span></div><a class="btn" href="#">More Info</a></div>
  <div class="solution abs" style="left:773px"><div class="solution-photo" role="img" aria-label="Conference hall with projected screens" style="background:linear-gradient(100deg,#3d4646,#8a8f8a 40%,#2f3434)"><span class="solution-caption">Medical Conferences</span></div><a class="btn" href="#">More Info</a></div>
</section>

<footer class="site-footer abs">Copyright@ Quorvia, 2017 | All Rights Reserved</footer>

</body>
</html>
```